American pesto sauce company needs a vintage/ old fashioned package design

Company name: Marisol Sauce.
We need a food label design for 4 different flavors of pesto sauce: classic almond, sundried tomato, roasted red pepper, and Cajun spice. For those that do not know what pesto is, it is a sauce like tomato sauce that is traditionally Italian and goes on pasta or whatever you choose to put it on and the consistent ingredients are garlic, cheese, nuts, olive oil and basil. They are fresh, all natural without preservatives, artificial flavors or colors.
The design of the jar is an old fashioned wire bale jar used for preserving foods ( attached is a picture). I'm looking for a label with:
• an upscale vintage feel but will also stand out on a grocery store shelf. I have attached an example of the feel I am looking for as well as the format of the words with my company name.
• The word "Pesto" must be prominent on the label.
• metalic gold boarders that go around the whole label maybe with gold embellishments if you see fit for that upscale feeling.
• Also, as you can see in the attachment, there are different typesets. And it must be easy to read from at least 3 feet away.
• Each label will have a different color corresponding to the flavor- could be part of the flavor text
• The bottom of the front panel must have “Net Wt. 5.75 oz (162g)” in a creative format how you see fit. Measures: height-28 mm, width-75mm
• Need logo for top part of label with the letters MS for Marisol Sauce and it will also contain the website, address and parent company name, use by date, etc. Measures:50 mm diameter
• The back panel of the label will contain the nutrition facts, ingredients and bar code. Measures: height-28 mm, width-75mm

Also the label is one piece with 3 different sections. Attached will be an example with measurements.
Updates

Check out this website on packaging. I absolutely love love love the Harwell Pantry almond water labels. The colors for the different flavors. How its not just horizontal or vertical. The different typesets/fonts/typography. The flourishes and background thats faded.
http://brightwrapgallery.com/page/3/

Target Market(s)

Target market is medium- high income foodies between 35-65

Industry/Entity Type

Grocery Store

Requirements
Must have
• Net Wt on front lower panel. Separation of the company name Marisol & Pesto. See attachment.
Nice to have
• Name of flavor designed in a wave pattern as shown in attachment. Hand drawn font OK.

```html
<!DOCTYPE html>
<html lang="en">
<head>
<meta charset="utf-8">
<title>Marisol Sauce – Lid Labels</title>
<link rel="stylesheet" href="https://fonts.googleapis.com/css2?family=Rye&family=Alegreya+Sans:wght@500;700;800&display=swap">
<style>
  :root {
    --page: #ffffff;
    --paper: #f8f2e2;
    --paper-rim: #f6efdc;
    --flourish: #e6d8bd;
    --basil: #3b5a2e;
    --red: #c1272d;
    --red-dark: #6b2a1f;
    --orange: #f47b20;
    --umber: #4a3b35;
    --sky: #9cc4cc;
    --slate: #3f5566;
    --tomato: #e0462c;
    --gold: #bfa878;
  }
  html, body {
    margin: 0;
    width: 1200px;
    height: 1000px;
    overflow: hidden;
    background: var(--page);
  }
  .label-sheet { display: block; width: 1200px; height: 1000px; }

  .disc { fill: var(--paper-rim); }
  .rim { fill: none; stroke: var(--ring); stroke-width: 4; }
  .pattern-band { fill: none; stroke: var(--pattern); stroke-width: 20; opacity: .45; }
  .pattern-edge { fill: none; stroke: var(--pattern); stroke-width: 1.5; }
  .field { fill: var(--paper); }
  .flourish { fill: var(--flourish); opacity: .7; }
  .care-note {
    font: 500 11px "Alegreya Sans", sans-serif;
    fill: var(--text);
    letter-spacing: .4px;
  }
  .monogram {
    font: 400 96px "Rye", serif;
    fill: var(--mark);
    text-anchor: middle;
  }
  .brand-name {
    font: 400 22px "Rye", serif;
    fill: var(--title);
    text-anchor: middle;
    letter-spacing: 1.2px;
  }
  .rule { stroke: var(--ribbon); stroke-width: 1.5; }
  .ribbon { fill: var(--ribbon); }
  .ribbon-text {
    font: 800 11.5px "Alegreya Sans", sans-serif;
    fill: #fff;
    text-anchor: middle;
    letter-spacing: .3px;
  }
  .contact, .use-by {
    font: 700 10.5px "Alegreya Sans", sans-serif;
    fill: var(--text);
    text-anchor: middle;
  }
  .use-by { font-weight: 500; font-size: 11.5px; }
  .swash { fill: var(--flourish); }

  .label--classic  { --ring: var(--red);    --pattern: var(--red);    --mark: var(--red);    --title: var(--red-dark); --ribbon: var(--red);    --text: var(--red); }
  .label--sundried { --ring: var(--orange); --pattern: var(--orange); --mark: var(--orange); --title: var(--umber);    --ribbon: var(--orange); --text: var(--orange); }
  .label--pepper   { --ring: var(--sky);    --pattern: var(--sky);    --mark: var(--sky);    --title: var(--slate);    --ribbon: var(--sky);    --text: var(--sky); }
  .label--cajun    { --ring: var(--gold);   --pattern: var(--tomato); --mark: var(--tomato); --title: var(--tomato);   --ribbon: var(--basil);  --text: var(--basil); }
</style>
</head>
<body>
<svg class="label-sheet" viewBox="0 0 1200 1000" xmlns="http://www.w3.org/2000/svg">
  <defs>
    <path id="care-arc" d="M -104,-100 A 145 145 0 0 1 104,-100"/>
  </defs>

  <g class="label label--classic" transform="translate(357 257)">
    <circle class="disc" r="205"/>
    <circle class="rim" r="189"/>
    <g role="img" aria-label="Decorative interlaced border pattern">
      <circle class="pattern-band" r="170"/>
      <circle class="pattern-edge" r="181"/>
      <circle class="pattern-edge" r="159"/>
    </g>
    <circle class="field" r="158"/>
    <g role="img" aria-label="Faded baroque leaf flourishes">
      <ellipse class="flourish" cx="-92" cy="-45" rx="46" ry="58"/>
      <ellipse class="flourish" cx="92" cy="-45" rx="46" ry="58"/>
    </g>
    <text class="care-note"><textPath href="#care-arc">Ready to eat. Keep refrigerated. OK to freeze.</textPath></text>
    <text class="monogram" x="0" y="10">MS</text>
    <text class="brand-name" x="0" y="42">MARISOL SAUCE</text>
    <line class="rule" x1="-140" y1="64" x2="-96" y2="64"/>
    <line class="rule" x1="96" y1="64" x2="140" y2="64"/>
    <path class="ribbon" d="M -100,56 L -88,56 L -88,52 L 88,52 L 88,56 L 100,56 L 94,64 L 100,72 L -100,72 L -94,64 Z"/>
    <text class="ribbon-text" x="0" y="66">ORCHARD LANE FOODS, LLC</text>
    <text class="contact" x="0" y="104">1820 Alder Ave. Riverton, NY 10999</text>
    <text class="contact" x="0" y="118">800-555-0142 &#160;www.marisolsauce.com</text>
    <g role="img" aria-label="Small swash ornaments">
      <ellipse class="swash" cx="-72" cy="137" rx="18" ry="4"/>
      <ellipse class="swash" cx="72" cy="137" rx="18" ry="4"/>
    </g>
    <text class="use-by" x="0" y="141">Use or freeze by</text>
    <text class="use-by" x="0" y="155">DD/MM/YYYY</text>
  </g>

  <g class="label label--sundried" transform="translate(820 265)">
    <circle class="disc" r="205"/>
    <circle class="rim" r="189"/>
    <g role="img" aria-label="Decorative interlaced border pattern">
      <circle class="pattern-band" r="170"/>
      <circle class="pattern-edge" r="181"/>
      <circle class="pattern-edge" r="159"/>
    </g>
    <circle class="field" r="158"/>
    <g role="img" aria-label="Faded baroque leaf flourishes">
      <ellipse class="flourish" cx="-92" cy="-45" rx="46" ry="58"/>
      <ellipse class="flourish" cx="92" cy="-45" rx="46" ry="58"/>
    </g>
    <text class="care-note"><textPath href="#care-arc">Ready to eat. Keep refrigerated. OK to freeze.</textPath></text>
    <text class="monogram" x="0" y="10">MS</text>
    <text class="brand-name" x="0" y="42">MARISOL SAUCE</text>
    <line class="rule" x1="-140" y1="64" x2="-96" y2="64"/>
    <line class="rule" x1="96" y1="64" x2="140" y2="64"/>
    <path class="ribbon" d="M -100,56 L -88,56 L -88,52 L 88,52 L 88,56 L 100,56 L 94,64 L 100,72 L -100,72 L -94,64 Z"/>
    <text class="ribbon-text" x="0" y="66">ORCHARD LANE FOODS, LLC</text>
    <text class="contact" x="0" y="104">1820 Alder Ave. Riverton, NY 10999</text>
    <text class="contact" x="0" y="118">800-555-0142 &#160;www.marisolsauce.com</text>
    <g role="img" aria-label="Small swash ornaments">
      <ellipse class="swash" cx="-72" cy="137" rx="18" ry="4"/>
      <ellipse class="swash" cx="72" cy="137" rx="18" ry="4"/>
    </g>
    <text class="use-by" x="0" y="141">Use or freeze by</text>
    <text class="use-by" x="0" y="155">DD/MM/YYYY</text>
  </g>

  <g class="label label--pepper" transform="translate(357 728)">
    <circle class="disc" r="205"/>
    <circle class="rim" r="189"/>
    <g role="img" aria-label="Decorative interlaced border pattern">
      <circle class="pattern-band" r="170"/>
      <circle class="pattern-edge" r="181"/>
      <circle class="pattern-edge" r="159"/>
    </g>
    <circle class="field" r="158"/>
    <g role="img" aria-label="Faded baroque leaf flourishes">
      <ellipse class="flourish" cx="-92" cy="-45" rx="46" ry="58"/>
      <ellipse class="flourish" cx="92" cy="-45" rx="46" ry="58"/>
    </g>
    <text class="care-note"><textPath href="#care-arc">Ready to eat. Keep refrigerated. OK to freeze.</textPath></text>
    <text class="monogram" x="0" y="10">MS</text>
    <text class="brand-name" x="0" y="42">MARISOL SAUCE</text>
    <line class="rule" x1="-140" y1="64" x2="-96" y2="64"/>
    <line class="rule" x1="96" y1="64" x2="140" y2="64"/>
    <path class="ribbon" d="M -100,56 L -88,56 L -88,52 L 88,52 L 88,56 L 100,56 L 94,64 L 100,72 L -100,72 L -94,64 Z"/>
    <text class="ribbon-text" x="0" y="66">ORCHARD LANE FOODS, LLC</text>
    <text class="contact" x="0" y="104">1820 Alder Ave. Riverton, NY 10999</text>
    <text class="contact" x="0" y="118">800-555-0142 &#160;www.marisolsauce.com</text>
    <g role="img" aria-label="Small swash ornaments">
      <ellipse class="swash" cx="-72" cy="137" rx="18" ry="4"/>
      <ellipse class="swash" cx="72" cy="137" rx="18" ry="4"/>
    </g>
    <text class="use-by" x="0" y="141">Use or freeze by</text>
    <text class="use-by" x="0" y="155">DD/MM/YYYY</text>
  </g>

  <g class="label label--cajun" transform="translate(822 728)">
    <circle class="disc" r="205"/>
    <circle class="rim" r="189"/>
    <g role="img" aria-label="Decorative interlaced border pattern">
      <circle class="pattern-band" r="170"/>
      <circle class="pattern-edge" r="181"/>
      <circle class="pattern-edge" r="159"/>
    </g>
    <circle class="field" r="158"/>
    <g role="img" aria-label="Faded baroque leaf flourishes">
      <ellipse class="flourish" cx="-92" cy="-45" rx="46" ry="58"/>
      <ellipse class="flourish" cx="92" cy="-45" rx="46" ry="58"/>
    </g>
    <text class="care-note"><textPath href="#care-arc">Ready to eat. Keep refrigerated. OK to freeze.</textPath></text>
    <text class="monogram" x="0" y="10">MS</text>
    <text class="brand-name" x="0" y="42">MARISOL SAUCE</text>
    <line class="rule" x1="-140" y1="64" x2="-96" y2="64"/>
    <line class="rule" x1="96" y1="64" x2="140" y2="64"/>
    <path class="ribbon" d="M -100,56 L -88,56 L -88,52 L 88,52 L 88,56 L 100,56 L 94,64 L 100,72 L -100,72 L -94,64 Z"/>
    <text class="ribbon-text" x="0" y="66">ORCHARD LANE FOODS, LLC</text>
    <text class="contact" x="0" y="104">1820 Alder Ave. Riverton, NY 10999</text>
    <text class="contact" x="0" y="118">800-555-0142 &#160;www.marisolsauce.com</text>
    <g role="img" aria-label="Small swash ornaments">
      <ellipse class="swash" cx="-72" cy="137" rx="18" ry="4"/>
      <ellipse class="swash" cx="72" cy="137" rx="18" ry="4"/>
    </g>
    <text class="use-by" x="0" y="141">Use or freeze by</text>
    <text class="use-by" x="0" y="155">DD/MM/YYYY</text>
  </g>
</svg>
</body>
</html>
```